RW Frameworks Inc Business cards

We need business cards using our existing logo but slightly modified. Right now the logo says RW Framework Masonry. We want to keep the RW part of the design, but replace the Framework Masonry portion with "FRAMEWORKS". Please see the attached file.
Ideally this would be a blank template so we can add Different Names, titles, and phone numbers later.
On the one side we want only the logo and on the other side the detail. I'm attaching an example for you to see.
Please reach out with any other questions. Our address and other details will be given out once we find a design we like.

Target Market(s)

Construction Industry

```html
<!DOCTYPE html>
<html lang="en">
<head>
<meta charset="utf-8">
<title>RW Frameworks Inc – Business Cards</title>
<link rel="stylesheet" href="https://fonts.googleapis.com/css2?family=Oswald:wght@500&family=Work+Sans:wght@400;500&display=swap">
<style>
  :root {
    --page-bg: #dde9f1;
    --card-white: #ffffff;
    --brand-blue: #1f76bc;
    --brand-grey: #838387;
    --silver: #d6d8db;
    --ink: #222326;
  }
  * { margin: 0; padding: 0; box-sizing: border-box; }
  html, body { width: 1200px; height: 1200px; overflow: hidden; }
  body {
    background: var(--page-bg);
    position: relative;
    font-family: "Work Sans", sans-serif;
  }
  .card {
    position: absolute;
    left: 283px;
    width: 634px;
    height: 362px;
    overflow: hidden;
  }
  .card--front { top: 174px; background: var(--card-white); }
  .card--back { top: 610px; background: var(--brand-blue); }

  .wordmark {
    position: absolute;
    font-family: "Work Sans", sans-serif;
    font-weight: 500;
    text-align: center;
    line-height: 1;
    white-space: nowrap;
  }
  .wordmark__initials { display: block; }
  .wordmark__name { display: block; }

  .card--front .wordmark {
    left: 72px; top: 94px; width: 204px;
    color: var(--brand-blue);
  }
  .card--front .wordmark__initials { font-size: 96px; letter-spacing: 3px; }
  .card--front .wordmark__name { margin-top: 2px; font-size: 14px; letter-spacing: 5px; }

  .card--back .wordmark {
    left: 142px; top: 86px; width: 350px;
    color: var(--silver);
  }
  .card--back .wordmark__initials { font-size: 150px; letter-spacing: 4px; }
  .card--back .wordmark__name { margin-top: 2px; font-size: 22px; letter-spacing: 9px; }

  .divider {
    position: absolute;
    left: 316px; top: 88px;
    width: 1px; height: 131px;
    background: var(--brand-blue);
  }
  .divider::before {
    content: ""; position: absolute; left: 0; top: 0;
    width: 3px; height: 22px; background: var(--brand-blue);
  }
  .contact { position: absolute; left: 343px; top: 86px; color: var(--ink); }
  .contact__name {
    font-family: "Oswald", sans-serif;
    font-weight: 500;
    font-size: 26px;
    line-height: 1.1;
    color: var(--brand-blue);
    letter-spacing: -0.3px;
  }
  .contact__title { font-size: 15px; }
  .contact__list { list-style: none; margin-top: 22px; }
  .contact__item {
    display: flex; align-items: center; gap: 9px;
    font-size: 16px; height: 21px;
  }
  .contact__icon { width: 12px; height: 12px; flex: none; }

  .card__swoosh { position: absolute; left: 0; top: 0; width: 634px; height: 362px; }
</style>
</head>
<body>

<section class="card card--front" aria-label="Business card front">
  <div class="wordmark">
    <span class="wordmark__initials">RW</span>
    <span class="wordmark__name">FRAMEWORKS</span>
  </div>

  <div class="divider"></div>

  <div class="contact">
    <h1 class="contact__name">RW BENNETT</h1>
    <p class="contact__title">Owner</p>
    <ul class="contact__list">
      <li class="contact__item">
        <svg class="contact__icon" viewBox="0 0 24 24" aria-hidden="true"><path fill="#1f76bc" d="M6.6 10.8a15.1 15.1 0 0 0 6.6 6.6l2.2-2.2c.3-.3.7-.4 1-.2 1.1.4 2.3.6 3.6.6.6 0 1 .4 1 1V20c0 .6-.4 1-1 1C10.6 21 3 13.4 3 4c0-.6.4-1 1-1h3.5c.6 0 1 .4 1 1 0 1.3.2 2.5.6 3.6.1.3 0 .7-.2 1z"/></svg>
        <span>+1 555 014 2290</span>
      </li>
      <li class="contact__item">
        <svg class="contact__icon" viewBox="0 0 24 24" aria-hidden="true"><path fill="#1f76bc" d="M2 5h20v14H2zm2 2v.5l8 5 8-5V7l-8 5z"/></svg>
        <span>rbennett@rwfw.com</span>
      </li>
      <li class="contact__item">
        <svg class="contact__icon" viewBox="0 0 24 24" aria-hidden="true"><g fill="none" stroke="#1f76bc" stroke-width="2"><circle cx="12" cy="12" r="9.5"/><ellipse cx="12" cy="12" rx="4" ry="9.5"/><path d="M2.5 12h19M4 7h16M4 17h16"/></g></svg>
        <span>www.rwfw.com</span>
      </li>
    </ul>
  </div>

  <svg class="card__swoosh" viewBox="0 0 1020 583" preserveAspectRatio="none" aria-hidden="true">
    <path fill="var(--brand-grey)" d="M107 513 Q510 383 914 513 Q510 403 107 513Z"/>
    <path fill="var(--brand-blue)" d="M0 558 Q510 394 1020 558 L1020 583 L0 583Z"/>
  </svg>
</section>

<section class="card card--back" aria-label="Business card back">
  <div class="wordmark">
    <span class="wordmark__initials">RW</span>
    <span class="wordmark__name">FRAMEWORKS</span>
  </div>
</section>

</body>
</html>
```